Logo and Business Card for Dental Office

We are opening a periodontal office (dental specialist for dental implants and gum diseases). It is a brand new state of the art facility with a focus on the most effective treatments for retaining natural teeth, or replacing teeth with implants when they must be lost. Strong emphasis on customer service and amenities for patient comfort. We are located just outside of Boston, MA.

Target Market(s)

potential adult patients, dentists in the community that will refer patients for specialized care

Industry/Entity Type

Dental

Requirements
Must have
• business name, address, phone number, website
Marcus T. Pellinger, DMD LLC
427 Corliss Street, Ste 305
Fenwick Glen, CT 06999
508-555-0172
508-555-0148 Fax
DrPellinger.example

the uploaded file has a rough version of what I'm looking for in the logo, I like the colors but it can be varies some.
Nice to have
• simple logo or symbol on business card, one possible idea I had was an abstract symbol of a screw or threads that might represent a dental implant, the attached file gives an idea of where to start.
Should not have
• I want a professional feel, no cartoons of teeth that appear childish, etc
The font should be easy to read with no curly/swirly shapes.

```html
<!DOCTYPE html>
<html lang="en">
<head>
<meta charset="utf-8">
<title>Periodontics &amp; Dental Implants — Business Card</title>
<link rel="stylesheet" href="https://fonts.googleapis.com/css2?family=Marcellus+SC&family=Cabin+Condensed:wght@400;500&display=swap">
<style>
  :root {
    --page-bg: #eceff1;
    --ink-dark: #14222c;
    --header-start: #00d6ef;
    --header-end: #55e2ef;
    --body-base: #00bcd4;
    --body-sheen: #45d0e0;
    --emblem-fill: #06b3cc;
    --text-light: #ffffff;
  }
  * { margin: 0; padding: 0; box-sizing: border-box; }
  html, body {
    width: 1200px;
    height: 1000px;
    overflow: hidden;
    background: var(--page-bg);
  }
  .business-card {
    position: absolute;
    left: 150px;
    top: 260px;
    width: 900px;
    height: 480px;
    background: var(--body-base);
    overflow: hidden;
    box-shadow: 0 10px 30px rgba(20, 34, 44, 0.18);
  }
  .card-surface {
    position: absolute;
    inset: 0;
    width: 100%;
    height: 100%;
  }
  .practice-title {
    position: absolute;
    top: 18px;
    right: 72px;
    width: 600px;
    text-align: center;
    font-family: "Marcellus SC", serif;
    font-size: 56px;
    line-height: 66px;
    font-weight: 400;
    color: var(--text-light);
    letter-spacing: 1px;
  }
  .emblem {
    position: absolute;
    left: -1px;
    top: -7px;
    width: 220px;
    height: 220px;
    border-radius: 50%;
    background: var(--emblem-fill);
    border: 10px solid var(--ink-dark);
    display: flex;
    align-items: center;
    justify-content: center;
  }
  .emblem-name {
    font-family: "Cabin Condensed", sans-serif;
    font-weight: 500;
    font-size: 34px;
    color: var(--text-light);
  }
  .contact-block {
    position: absolute;
    right: 59px;
    top: 210px;
    text-align: right;
    font-family: "Cabin Condensed", sans-serif;
    color: var(--text-light);
  }
  .doctor-name {
    font-size: 46px;
    font-weight: 400;
    line-height: 56px;
    margin-bottom: 32px;
  }
  .contact-line {
    font-size: 26px;
    line-height: 40px;
  }
  .contact-divider { margin: 0 6px 0 10px; }
</style>
</head>
<body>
  <main class="business-card">
    <svg class="card-surface" viewBox="0 0 900 480" aria-hidden="true">
      <defs>
        <linearGradient id="header-gradient" x1="0" y1="0" x2="1" y2="0">
          <stop offset="0" stop-color="var(--header-start)"/>
          <stop offset="1" stop-color="var(--header-end)"/>
        </linearGradient>
      </defs>
      <rect x="0" y="0" width="900" height="174" fill="url(#header-gradient)"/>
      <path d="M118 480 C 190 300, 340 120, 562 0 L 900 0 L 900 480 Z" fill="var(--body-sheen)" opacity="0.55"/>
      <rect x="0" y="174" width="900" height="9" fill="var(--ink-dark)"/>
    </svg>

    <div class="emblem">
      <span class="emblem-name">Pellinger</span>
    </div>

    <h1 class="practice-title">Periodontics &amp;<br>Dental Implants</h1>

    <section class="contact-block">
      <p class="doctor-name">Marcus T. Pellinger, DMD LLC</p>
      <p class="contact-line">427 Corliss Street, Ste 305</p>
      <p class="contact-line">Fenwick Glen, CT 06999</p>
      <p class="contact-line">Phone: 508-555-0172<span class="contact-divider">|</span>Fax: 508-555-0148</p>
      <p class="contact-line">www.DrPellinger.example</p>
    </section>
  </main>
</body>
</html>
```